Personal Chef Needs a Good Web Design

Hi everyone!
My name is Teo, I work as a private chef for last 10 years, traveling all around the world and cooking in private megayacht and villas.
I'm about to settle down in my hometown in Europe for a while. And therefore I need a website that will show my story, pics and recipes, nutritional advices and of course offer a Personal and Private Chef services( working for 4-5 families and bringing delicious food to their house).
My clients are extremely rich folks, but usually are down to earth ones.
I believe, the web site should be focused on attention to:
-VIP person's wife( as she is usually responsible for food for family) and be simple.
-to famous people agents and be on high level.

There will be about 10 different menus and 6 different service offers

--UPDATE--
Logo Design:
+My thoughts are- printed structure of the vegetable or fruit on a white font. Like you slice the buffalo tomato, put it in red paint and print it on the edge of the page. See attached files named logo. Can be any nice structured thing, like tomato, lemon, red cabbage etc.
+Classic logos with chef's hat or knives are good too.
+Need to have the space for me to add the name( the fonts can be provided)

Target Market(s)

Private person. 80% Russian clients.

Industry/Entity Type

Cooking

Coding

Coded - Design and coding required

Number of Pages Required

3 page

Requirements
Must have
• Contact form/ Request back call/ Schedule a free consultation
Nice to have
• The client will need to choose straight ahead from the range of services I offer, like:
• -Private Chef( cooking only for the client)
• -Personal Chef( cooking for around 5 clients, bringing the ready to be heated food to their door)
• -Romantic dinner for two
• -Professional Sommelier service
• -Build your kitchen( offering design, equipment and that will fit your requirements)
• -Other( flowers, waiters, barista, equipment rental)
• So this column should go right after the introduction/aboutme part and will lead to separate pages with how-it-works thing for each.

```html
<!DOCTYPE html>
<html lang="en">
<head>
<meta charset="utf-8">
<title>Teo Table — Our Services</title>
<link rel="stylesheet" href="https://fonts.googleapis.com/css2?family=Nunito+Sans:wght@400;600;700&family=Open+Sans:wght@400&display=swap">
<style>
  :root {
    --ink: #1b1b1b;
    --text: #5a5a5a;
    --rule: #d6d6d6;
    --frame: #a9a9a9;
    --accent: #e0914a;
    --icon: #a3a3a3;
    --paper: #ffffff;
  }
  * { box-sizing: border-box; margin: 0; padding: 0; }
  html, body { width: 1200px; height: 2594px; overflow: hidden; background: var(--paper); }
  body { font-family: "Open Sans", sans-serif; color: var(--text); position: relative; }

  .site-header {
    height: 81px; border-bottom: 1px solid var(--rule);
    display: flex; align-items: center; justify-content: space-between;
    padding: 0 99px 0 98px;
  }
  .brand { font-family: "Nunito Sans", sans-serif; font-weight: 600; font-size: 24px; color: var(--ink); }
  .menu-toggle { width: 34px; height: 34px; display: block; }

  .page-title {
    font-family: "Nunito Sans", sans-serif; font-weight: 600; font-size: 33px;
    color: var(--ink); text-align: center; letter-spacing: 0.5px;
    height: 90px; line-height: 124px;
  }

  .services { width: 1006px; margin: 0 auto 0 96px; }
  .service {
    height: 383px; border-bottom: 1px solid var(--rule);
    display: flex; align-items: flex-start; padding-top: 33px;
  }
  .service:last-child { border-bottom: none; }
  .service--right { flex-direction: row-reverse; }

  .service-photo {
    width: 347px; height: 320px; border: 1px solid var(--frame);
    padding: 5px; flex: none; background: var(--paper);
  }
  .service-photo span { display: block; width: 100%; height: 100%; }

  .service-body { width: 602px; margin-left: 55px; padding-top: 5px; }
  .service--right .service-body { margin-left: 0; margin-right: 57px; }

  .service-title {
    font-family: "Nunito Sans", sans-serif; font-weight: 600; font-size: 28px;
    color: var(--ink); line-height: 40px; margin-bottom: 18px;
  }
  .service-body p { font-size: 11.2px; line-height: 31.5px; }
  .service-body p + p { margin-top: 32px; }

  .tone-kitchen { background: linear-gradient(135deg, #5a4a3c, #d9d6d2 55%, #8a7a6a); }
  .tone-dining  { background: linear-gradient(135deg, #d8d2ca, #f1ece8 45%, #b58a6a); }
  .tone-romance { background: linear-gradient(160deg, #8b3a2a, #d8b070 45%, #3a2a20); }
  .tone-wine    { background: linear-gradient(160deg, #4a3626, #a88060 40%, #2a2a30); }
  .tone-cooking { background: linear-gradient(135deg, #c9b6a0, #e8dccc 50%, #7c9a55); }
  .tone-plate   { background: linear-gradient(160deg, #d8d4cf, #b8a898 45%, #c85a2a); }

  .site-footer {
    position: absolute; left: 0; right: 0; top: 2505px; height: 89px;
    border-top: 5px solid var(--accent);
    display: flex; align-items: center; justify-content: space-between;
    padding: 0 99px 0 98px;
  }
  .copyright { font-size: 11.2px; color: var(--text); }
  .social { display: flex; gap: 12px; list-style: none; }
  .social li { width: 27px; height: 27px; border-radius: 4px; background: var(--icon); }
</style>
</head>
<body>
  <header class="site-header">
    <div class="brand">Teo Table</div>
    <svg class="menu-toggle" viewBox="0 0 34 34" aria-label="Menu">
      <circle cx="17" cy="17" r="16" fill="none" stroke="#b9b9b9" stroke-width="1.2"/>
      <g stroke="var(--accent)" stroke-width="2" stroke-linecap="round">
        <line x1="12.5" y1="13.5" x2="21.5" y2="13.5"/>
        <line x1="12.5" y1="17" x2="21.5" y2="17"/>
        <line x1="12.5" y1="20.5" x2="21.5" y2="20.5"/>
      </g>
    </svg>
  </header>

  <main>
    <h1 class="page-title">OUR SERVICES</h1>

    <section class="services">
      <article class="service">
        <div class="service-photo"><span class="tone-kitchen" role="img" aria-label="Chef in white jacket standing in a bakery kitchen"></span></div>
        <div class="service-body">
          <h2 class="service-title">Private Chef</h2>
          <p>At vero eos et accusamus et iusto odio dignissimos ducimus qui blanditiis praesentium voluptatum deleniti at quae corrupti quos dolores et quas molestias excepturi.</p>
          <p>Sint occaecati cupiditate non provident, similique sunt in culpa qui officia deserunt mollitia animi, id est laborum et dolorum fuga. Et harum quidem rerum facilis est et expedita distinctio. Nam libero tempore, cum soluta nobis est eligendi optio cumque nihil impedit quo minus id quod epudiandae sint et molestiae nore cusandae. Itaque earum rerum hic tenetur a sapiente delectus, ut aut reiciendis voluptatibus maiores alias consequatur aut perferendis doloribus asperiores repella.</p>
        </div>
      </article>

      <article class="service service--right">
        <div class="service-photo"><span class="tone-dining" role="img" aria-label="Chef serving a plate to guests at a dining table"></span></div>
        <div class="service-body">
          <h2 class="service-title">Personal Chef</h2>
          <p>At vero eos et accusamus et iusto odio dignissimos ducimus qui blanditiis praesentium voluptatum deleniti at quae corrupti quos dolores et quas molestias excepturi.</p>
          <p>Sint occaecati cupiditate non provident, similique sunt in culpa qui officia deserunt mollitia animi, id est laborum et dolorum fuga. Et harum quidem rerum facilis est et expedita distinctio. Nam libero tempore, cum soluta nobis est eligendi optio cumque nihil impedit quo minus id quod epudiandae sint et molestiae nore cusandae. Itaque earum rerum hic tenetur a sapiente delectus, ut aut reiciendis voluptatibus maiores alias consequatur aut perferendis doloribus asperiores repella.</p>
        </div>
      </article>

      <article class="service">
        <div class="service-photo"><span class="tone-romance" role="img" aria-label="Couple toasting with wine over a seafood dish"></span></div>
        <div class="service-body">
          <h2 class="service-title">Romantic Dinner for two</h2>
          <p>At vero eos et accusamus et iusto odio dignissimos ducimus qui blanditiis praesentium voluptatum deleniti at quae corrupti quos dolores et quas molestias excepturi.</p>
          <p>Sint occaecati cupiditate non provident, similique sunt in culpa qui officia deserunt mollitia animi, id est laborum et dolorum fuga. Et harum quidem rerum facilis est et expedita distinctio. Nam libero tempore, cum soluta nobis est eligendi optio cumque nihil impedit quo minus id quod epudiandae sint et molestiae nore cusandae. Itaque earum rerum hic tenetur a sapiente delectus, ut aut reiciendis voluptatibus maiores alias consequatur aut perferendis doloribus asperiores repella.</p>
        </div>
      </article>

      <article class="service service--right">
        <div class="service-photo"><span class="tone-wine" role="img" aria-label="Sommelier holding up a glass of red wine in a wine cellar"></span></div>
        <div class="service-body">
          <h2 class="service-title">Professional Sommelier</h2>
          <p>At vero eos et accusamus et iusto odio dignissimos ducimus qui blanditiis praesentium voluptatum deleniti at quae corrupti quos dolores et quas molestias excepturi.</p>
          <p>Sint occaecati cupiditate non provident, similique sunt in culpa qui officia deserunt mollitia animi, id est laborum et dolorum fuga. Et harum quidem rerum facilis est et expedita distinctio. Nam libero tempore, cum soluta nobis est eligendi optio cumque nihil impedit quo minus id quod epudiandae sint et molestiae nore cusandae. Itaque earum rerum hic tenetur a sapiente delectus, ut aut reiciendis voluptatibus maiores alias consequatur aut perferendis doloribus asperiores repella.</p>
        </div>
      </article>

      <article class="service">
        <div class="service-photo"><span class="tone-cooking" role="img" aria-label="People preparing vegetables together in a bright home kitchen"></span></div>
        <div class="service-body">
          <h2 class="service-title">Build your Kitchen</h2>
          <p>At vero eos et accusamus et iusto odio dignissimos ducimus qui blanditiis praesentium voluptatum deleniti at quae corrupti quos dolores et quas molestias excepturi.</p>
          <p>Sint occaecati cupiditate non provident, similique sunt in culpa qui officia deserunt mollitia animi, id est laborum et dolorum fuga. Et harum quidem rerum facilis est et expedita distinctio. Nam libero tempore, cum soluta nobis est eligendi optio cumque nihil impedit quo minus id quod epudiandae sint et molestiae nore cusandae. Itaque earum rerum hic tenetur a sapiente delectus, ut aut reiciendis voluptatibus maiores alias consequatur aut perferendis doloribus asperiores repella.</p>
        </div>
      </article>

      <article class="service service--right">
        <div class="service-photo"><span class="tone-plate" role="img" aria-label="Chef presenting a colourful plated vegetable dish"></span></div>
        <div class="service-body">
          <h2 class="service-title">Other Services</h2>
          <p>At vero eos et accusamus et iusto odio dignissimos ducimus qui blanditiis praesentium voluptatum deleniti at quae corrupti quos dolores et quas molestias excepturi.</p>
          <p>Sint occaecati cupiditate non provident, similique sunt in culpa qui officia deserunt mollitia animi, id est laborum et dolorum fuga. Et harum quidem rerum facilis est et expedita distinctio. Nam libero tempore, cum soluta nobis est eligendi optio cumque nihil impedit quo minus id quod epudiandae sint et molestiae nore cusandae. Itaque earum rerum hic tenetur a sapiente delectus, ut aut reiciendis voluptatibus maiores alias consequatur aut perferendis doloribus asperiores repella.</p>
        </div>
      </article>
    </section>
  </main>

  <footer class="site-footer">
    <p class="copyright">Copyrights © 2016, Teo Table . All Rights Reserved.</p>
    <ul class="social" aria-label="Social links">
      <li></li><li></li><li></li><li></li>
    </ul>
  </footer>
</body>
</html>
```